Nine Rung Ledger Remedy Seminar

I would like a flyer to hand out to participants at the speeches that we give. We are a CPA firm that specializes in entrepreneurs and realtors. We would like a flyer that looks crisp and clean, that integrates our logo and our company colors (shades of blue & gold). We would like the wording to be as laid out in the attached documents, but design is up to you. We would like a picture to go along with each point and are open to ideas. The flyer should be one page, preferably just the front.

Colors
3176b5
fee18a

Requirements
Must have
• Our logo and the wording supplied.
• A picture to go along with each topic.
Nice to have
• Images that pop, clean look, professional.
Should not have
• Look messy.

```html
<!DOCTYPE html>
<html lang="en">
<head>
<meta charset="utf-8">
<title>Nine Rung Ledger Remedy Seminar Agenda</title>
<link rel="stylesheet" href="https://fonts.googleapis.com/css2?family=Montserrat:wght@400;500;600;700;800&family=Lora:ital,wght@1,600&display=swap">
<style>
  :root {
    --blue: #2a57a5;
    --blue-deep: #1f4690;
    --band: #3176b5;
    --gold: #f0cc7c;
    --gold-edge: #d9b260;
    --gold-title: #e3a21f;
    --ink: #2e2e2e;
    --paper: #f1f2f4;
    --page: #e4e4e4;
  }
  * { box-sizing: border-box; margin: 0; padding: 0; }
  html, body { width: 1200px; height: 1200px; overflow: hidden; background: var(--page); }
  body { position: relative; font-family: "Montserrat", sans-serif; color: var(--ink); }

  .flyer {
    position: absolute; left: 180px; top: 8px; width: 840px; height: 1184px;
    background: linear-gradient(180deg, #f6f7f8 0%, var(--paper) 50%, #eceef1 100%);
    box-shadow: 0 4px 18px rgba(0,0,0,.18);
    overflow: hidden;
  }

  .brand { position: absolute; top: 52px; left: 0; width: 100%; text-align: center; }
  .brand-name { font-weight: 800; font-size: 44px; color: var(--blue); letter-spacing: -0.5px; line-height: 1; }
  .brand-tagline { margin-top: 22px; font-family: "Lora", serif; font-style: italic; font-weight: 600; font-size: 12px; color: #222; }

  .agenda-title {
    position: absolute; top: 160px; left: 0; width: 100%; text-align: center;
    font-size: 22px; font-weight: 700; color: var(--blue); letter-spacing: .2px;
  }
  .agenda-title .accent { color: var(--gold-title); }

  .step { position: absolute; left: 0; width: 840px; height: 100px; }
  .step-pill {
    position: absolute; top: 0; height: 100px; border-radius: 50px;
    background: var(--gold); border: 2px solid var(--gold-edge);
    box-shadow: 0 3px 4px rgba(0,0,0,.12);
  }
  .step-num {
    position: absolute; top: -6px; width: 112px; height: 112px; border-radius: 50%;
    background: #fff; border: 7px solid var(--blue);
    box-shadow: 0 0 0 3px #fff, 0 3px 6px rgba(0,0,0,.25);
    display: flex; align-items: center; justify-content: center;
    font-size: 42px; font-weight: 500; color: var(--blue); letter-spacing: 1px;
  }
  .step-text {
    position: absolute; top: 0; height: 100px; width: 466px;
    display: flex; align-items: center;
    font-size: 12.4px; line-height: 15.3px; text-align: justify; color: #2b2b2b;
  }
  .step-divider { position: absolute; top: 8px; width: 1px; height: 84px; background: rgba(120,90,30,.35); }
  .step-icon { position: absolute; top: 25px; width: 52px; height: 50px; }
  .step-icon svg { width: 52px; height: 50px; }

  .step.odd .step-pill { left: 100px; width: 688px; }
  .step.odd .step-num { left: 52px; }
  .step.odd .step-text { left: 183px; }
  .step.odd .step-divider { left: 673px; }
  .step.odd .step-icon { left: 705px; }

  .step.even .step-pill { left: 52px; width: 688px; }
  .step.even .step-num { left: 676px; }
  .step.even .step-text { left: 186px; }
  .step.even .step-divider { left: 163px; }
  .step.even .step-icon { left: 82px; }

  .slogan {
    position: absolute; top: 1084px; left: 0; width: 100%; text-align: center;
    font-size: 19px; font-weight: 600; color: #333; letter-spacing: .3px;
  }
  .slogan strong { color: var(--blue); font-weight: 700; }

  .contact-band {
    position: absolute; left: 0; top: 1124px; width: 100%; height: 52px;
    background: var(--band); color: #fff; font-size: 12px;
  }
  .contact-item { position: absolute; display: flex; align-items: center; gap: 8px; }
  .contact-item svg { width: 16px; height: 14px; flex: none; }
</style>
</head>
<body>
<main class="flyer">
  <header class="brand">
    <div class="brand-name">Tallyward Figures</div>
    <div class="brand-tagline">A Professional Accounting Corporation</div>
  </header>

  <h1 class="agenda-title"><span class="accent">Nine Rung</span> Ledger Remedy Seminar Agenda:</h1>

  <section class="step odd" style="top:205px">
    <div class="step-pill"></div>
    <div class="step-num">01</div>
    <p class="step-text">We will first show you how to eliminate much of your self-employment tax on your return by converting your business into an S Corporation. A business owner making over $120,000 per year can save about $12,000 per year by doing this.</p>
    <div class="step-divider"></div>
    <div class="step-icon"><svg viewBox="0 0 52 50" fill="none" stroke="#333" stroke-width="2.4"><rect x="4" y="10" width="44" height="32" rx="2"/><path d="M18 10v-5h16v5"/><circle cx="26" cy="26" r="8" fill="#333"/><path d="M23 23l6 6M29 23l-6 6" stroke="#f0cc7c"/></svg></div>
  </section>

  <section class="step even" style="top:330px">
    <div class="step-pill"></div>
    <div class="step-num">02</div>
    <div class="step-divider"></div>
    <div class="step-icon"><svg viewBox="0 0 52 50" fill="#333"><path d="M8 18h36l-13 14v14l-10-6v-8z"/><path d="M14 14l6-9 5 8 5-8 6 9z" fill="none" stroke="#333" stroke-width="2.2"/></svg></div>
    <p class="step-text">We will show you how to get tax free income from your corporation by renting you home to the corporation for the board meetings. Many of our clients are getting up to $21,000 in tax free income which could put $8,400 cash into your pocket.</p>
  </section>

  <section class="step odd" style="top:455px">
    <div class="step-pill"></div>
    <div class="step-num">03</div>
    <p class="step-text">We will show you the easiest way to track your expenses so that the only thing you will have to do to have rock solid books is to take a picture of the receipt and throw it away. It doesn't get any better than that.</p>
    <div class="step-divider"></div>
    <div class="step-icon"><svg viewBox="0 0 52 50" fill="none" stroke="#333" stroke-width="2.4"><rect x="9" y="5" width="34" height="43" rx="2"/><rect x="19" y="1" width="14" height="7" fill="#333"/><path d="M15 16h22M15 22h22M15 28h22M15 34h22M15 40h16"/></svg></div>
  </section>

  <section class="step even" style="top:580px">
    <div class="step-pill"></div>
    <div class="step-num">04</div>
    <div class="step-divider"></div>
    <div class="step-icon"><svg viewBox="0 0 52 50" fill="none" stroke="#333" stroke-width="2.2"><path d="M8 3h28l9 9v36H8z"/><rect x="27" y="13" width="9" height="7"/><path d="M31 20v7H18v8M31 27v8"/><circle cx="18" cy="38" r="3"/><circle cx="31" cy="38" r="3"/></svg></div>
    <p class="step-text">Next, we show you the importance of tax planning and why it is critical to meet with your CPA before the end of the year and not just when you do your tax preparation.</p>
  </section>

  <section class="step odd" style="top:704px">
    <div class="step-pill"></div>
    <div class="step-num">05</div>
    <p class="step-text">We will show you how to hire your children and get $7,500 per child tax free. This will save you $3,000 per child in income tax reduction.</p>
    <div class="step-divider"></div>
    <div class="step-icon"><svg viewBox="0 0 52 50" fill="#333"><circle cx="14" cy="9" r="5"/><path d="M7 17h14l-2 14h-2v15h-6V31H9z"/><circle cx="38" cy="9" r="5"/><path d="M32 17h12l5 20h-5v9h-10v-9h-5z"/></svg></div>
  </section>

  <section class="step even" style="top:829px">
    <div class="step-pill"></div>
    <div class="step-num">06</div>
    <div class="step-divider"></div>
    <div class="step-icon"><svg viewBox="0 0 52 50" fill="none" stroke="#333" stroke-width="2.2"><rect x="6" y="5" width="30" height="42" rx="2"/><path d="M10 9v34h22"/><rect x="14" y="18" width="14" height="9"/><path d="M42 6v36l-2 5-2-5V6z"/></svg></div>
    <p class="step-text">We will discuss how to make your child's college education tax deductible. With college cost spiraling out of control this is a biggie. Most of our clients have a savings of about $12,000 per year of college.</p>
  </section>

  <section class="step odd" style="top:954px">
    <div class="step-pill"></div>
    <div class="step-num">07</div>
    <p class="step-text">Our grand finale is to show you how to use, not one, but two corporations to get a several hundred thousand dollar tax deferral, get an interest free loan from the government and use that money to grow your business and your wealth.</p>
    <div class="step-divider"></div>
    <div class="step-icon"><svg viewBox="0 0 52 50" fill="none" stroke="#333" stroke-width="2.2"><path d="M30 8h12l-3 6c8 4 10 12 6 18-3 4-11 4-15 0"/><circle cx="16" cy="34" r="13"/><path d="M10 20l2-5h8l2 5"/><text x="16" y="40" font-family="Montserrat, sans-serif" font-size="15" font-weight="700" fill="#333" stroke="none" text-anchor="middle">$</text><text x="38" y="28" font-family="Montserrat, sans-serif" font-size="13" font-weight="700" fill="#333" stroke="none" text-anchor="middle">$</text></svg></div>
  </section>

  <p class="slogan">If they drive by with a machine gun <strong>you don't have to stand up.</strong></p>

  <footer class="contact-band">
    <div class="contact-item" style="left:50px; top:7px">
      <svg viewBox="0 0 16 14" fill="#f0cc7c"><path d="M8 0l8 7h-2v7H10V9H6v5H2V7H0z"/></svg>
      820 E. Orchard Ave, Ste. B, Linden Vale, CA 90000
    </div>
    <div class="contact-item" style="left:50px; top:31px">
      <svg viewBox="0 0 16 16" fill="none" stroke="#f0cc7c" stroke-width="1.4"><circle cx="8" cy="8" r="7"/><ellipse cx="8" cy="8" rx="3" ry="7"/><path d="M1 8h14"/></svg>
      www.tallywardcpa.example
    </div>
    <div class="contact-item" style="left:380px; top:7px">
      <svg viewBox="0 0 16 14" fill="#f0cc7c"><path d="M1 4c0-3 14-3 14 0v2h-4V4H5v2H1z"/><rect x="3" y="7" width="10" height="7" rx="1"/></svg>
      555-014-2231
    </div>
    <div class="contact-item" style="left:380px; top:31px">
      <svg viewBox="0 0 16 14" fill="#f0cc7c"><rect x="4" y="0" width="8" height="5"/><rect x="1" y="5" width="14" height="9" rx="1"/></svg>
      555-014-2240
    </div>
    <div class="contact-item" style="left:570px; top:7px">
      <svg viewBox="0 0 16 12" fill="none" stroke="#f0cc7c" stroke-width="1.4"><rect x="1" y="1" width="14" height="10"/><path d="M1 1l7 6 7-6"/></svg>
      Wendell@tallywardcpas.example
    </div>
    <div class="contact-item" style="left:570px; top:31px">
      <svg viewBox="0 0 16 12" fill="none" stroke="#f0cc7c" stroke-width="1.4"><rect x="1" y="1" width="14" height="10"/><path d="M1 1l7 6 7-6"/></svg>
      Maris@tallywardcpas.example
    </div>
  </footer>
</main>
</body>
</html>
```